kVista Corporate Website

kVista is a well-funded start up developing an Online Marketing Platform for small businesses in Europe.
We are launching in February 2012 with all-in-one online marketing services including professional website, DIY SEO, Dashboard with Reports and Online marketing tools, and Support.
Our internal web designer has come up with a preliminary website design which we wish to continue to improve using new ideas, colours, layout, image, etc.
The brief is very simple - improve the website whether it is look & feel, ease of use, conversion rate - we are looking for overall improvements.
The contest will last 5 days and we will award the winner £300.
If you are the winner , you will also be required to provide designs for 3 more internal pages adhering to the proposed home page design.
Judging criteria : -
Visual Design
Layout must adhere to best practices and wire frame. If you decide to move elements around significantly please provide reason
Functional, informative and drives calls to action
Industry/Entity Type
Marketing
Look and feel
Each slider illustrates characteristics of the customer's brand and the style your logo design should communicate.

```html
<!DOCTYPE html>
<html lang="en">
<head>
<meta charset="utf-8">
<title>kVista – Online Marketing Platform for Small Business</title>
<link rel="stylesheet" href="https://fonts.googleapis.com/css2?family=Arimo:wght@400;700&family=Didact+Gothic&display=swap">
<style>
:root{
  --blue:#5bc3e8;
  --blue-dark:#3aa9d6;
  --ink:#333;
  --muted:#777;
  --panel:#8d8d8d;
  --panel-line:#a9a9a9;
  --side:#d9d9d9;
  --header-top:#f2f2f2;
  --header-bottom:#dedede;
  --footer:#d4d4d4;
  --bubble-border:#b9c9d1;
  --white:#fff;
}
*{box-sizing:border-box;margin:0;padding:0}
html,body{width:819px;height:1200px;overflow:hidden}
body{position:relative;background:var(--white);font-family:"Arimo",Arial,sans-serif;color:var(--ink);font-size:9px}
.abs{position:absolute}
a{color:inherit;text-decoration:none}

.site-header{left:0;top:0;width:819px;height:97px;background:linear-gradient(var(--header-top),var(--header-bottom))}
.account-links{right:34px;top:3px;font-size:9.5px;color:#333}
.account-links span{margin:0 7px;color:#666}
.brand{display:flex;align-items:center;gap:5px;font-family:"Didact Gothic",sans-serif;color:#444}
.brand-dot{border-radius:50%;border:3px solid var(--blue)}
.site-header .brand{left:38px;top:34px;font-size:23px}
.site-header .brand-dot{width:22px;height:22px}
.main-nav{left:191px;top:34px;width:602px;height:27px;background:var(--blue);border-radius:3px;display:flex;align-items:center;padding-left:11px;font-size:10.5px;color:var(--white)}
.main-nav a{margin-right:11px}
.main-nav .sep{margin-right:11px}
.search{position:absolute;right:6px;top:4px;width:135px;height:18px;background:var(--white);border-radius:2px}
.search svg{position:absolute;left:5px;top:4px}

.hero-photo{left:298px;top:155px;width:217px;height:210px;background:radial-gradient(ellipse at 50% 40%,#e4b79b,#a26a4c 60%,#4a3226);border-radius:100px 100px 0 0}
.bubble{position:absolute;height:34px;background:linear-gradient(#fff,#e9eff2);border:1px solid var(--bubble-border);border-radius:4px;font-size:11.5px;color:#333;display:flex;align-items:center;justify-content:center}
.bubble::after{content:"";position:absolute;bottom:-7px;width:8px;height:8px;background:#ebf0f3;border-right:1px solid var(--bubble-border);border-bottom:1px solid var(--bubble-border);transform:skewY(45deg)}

.slider{left:34px;top:365px;width:745px;height:84px;border:1px solid #ccc;border-radius:3px;background:linear-gradient(#fff,#eee)}
.slider h1{position:absolute;left:23px;top:18px;font-family:"Didact Gothic",sans-serif;font-weight:400;font-size:20.5px;color:#222}
.slider p{position:absolute;left:23px;top:47px;font-family:"Didact Gothic",sans-serif;font-size:15px;color:var(--blue)}
.learn-more{position:absolute;right:10px;top:15px;padding:2px 4px;border:1px solid #aaa;border-radius:3px;background:linear-gradient(#fafafa,#ddd);font-size:10px;color:#444}
.dots{position:absolute;right:7px;top:68px;display:flex;gap:5px}
.dots i{width:8px;height:8px;border-radius:50%;background:var(--blue)}
.dots i:first-child{background:#111}

.welcome{left:37px;top:467px;width:485px}
.welcome h2{display:flex;align-items:center;gap:4px;font-family:"Didact Gothic",sans-serif;font-weight:400;font-size:18px;color:#555;margin-bottom:10px}
.welcome h2 em{font-style:italic;color:#777}
.welcome .brand-dot{width:17px;height:17px;border-width:2.5px}
.welcome p{font-size:8.6px;line-height:11.4px;color:#777;margin-bottom:10px}
.welcome p.narrow{width:310px}
.sign-photo{left:382px;top:463px;width:110px;height:110px;background:linear-gradient(#f3f3f3,#9fb5cf 60%,#2c2c2c)}

.news-box{left:557px;top:463px;width:217px;height:270px;background:var(--side);border-radius:4px}
.news-box h3{position:absolute;left:8px;top:12px;width:205px;font-weight:400;font-size:11.5px;line-height:14px;color:#111}
.badge{position:absolute;background:linear-gradient(#f4f4f4,#c9c9c9);border:1px solid #bbb}
.news-box .cap{position:absolute;font-size:8.5px;color:#444;line-height:10.5px}

.features{left:38px;top:756px;width:742px;height:216px;background:var(--panel);border-radius:4px;display:flex}
.feature{position:relative;flex:none;padding:0 9px 0 20px;color:var(--white);border-right:1px solid var(--panel-line)}
.feature:last-child{border:none}
.feature h4{font-family:"Didact Gothic",sans-serif;font-style:italic;font-weight:700;font-size:14px;color:#6f6f6f;margin-top:23px;letter-spacing:.3px}
.feature h5{font-family:"Didact Gothic",sans-serif;font-style:italic;font-weight:700;font-size:11px;color:var(--blue);margin-top:23px;line-height:12px}
.feature p{font-size:8.6px;line-height:11px;margin-top:8px}
.feature .icon{position:absolute;right:18px;top:18px;width:42px;height:50px;border-radius:6px}

.site-footer{left:0;top:986px;width:819px;height:214px;background:linear-gradient(#dcdcdc,#c8c8c8);border-top:3px solid var(--blue)}
.site-footer h6{font-family:"Didact Gothic",sans-serif;font-style:italic;font-weight:400;font-size:12px;color:#666}
.footer-col{position:absolute;top:28px}
.footer-col ul{list-style:none;margin-top:8px;margin-left:4px;font-size:8.8px;line-height:14.6px;color:#333}
.social{display:grid;grid-template-columns:28px 28px;gap:6px 5px;margin-top:10px}
.social i{width:28px;height:28px;border-radius:3px;background:#3b63a8}
.social i:nth-child(2){background:#3fa7dd}
.social i:nth-child(3){background:#e8731c}
.social i:nth-child(4){background:#c8c8c8;border:1px solid #999}
.newsletter{position:absolute;left:545px;top:20px}
.newsletter h6{letter-spacing:.5px;font-size:11px}
.nl-form{display:flex;gap:5px;margin-top:16px}
.nl-form span{width:174px;height:22px;background:var(--white);border:1px solid var(--blue)}
.nl-form b{width:88px;height:22px;background:var(--blue);color:var(--white);font-weight:400;font-size:10px;display:flex;align-items:center;justify-content:center}
.mailbox{left:555px;top:1090px;width:65px;height:86px;background:linear-gradient(#777,#333);border-radius:20px 20px 4px 4px}
.about-note{left:630px;top:1086px;width:175px;font-size:8.5px;line-height:10.5px;color:#555}
.about-note .brand{font-size:11.5px;margin:3px 0 1px;color:#444}
.about-note .brand-dot{width:11px;height:11px;border-width:2px}
.legal{left:105px;top:1178px;font-size:8.5px;color:#333}
.legal a{color:var(--blue);margin-left:18px}
.legal .sep{color:#888;margin-left:12px}
</style>
</head>
<body>

<header class="site-header abs">
  <div class="account-links abs"><a href="#">Login</a><span>|</span><a href="#">Register</a></div>
  <div class="brand abs"><span class="brand-dot"></span>kVista</div>
  <nav class="main-nav abs">
    <a href="#">Home</a><span class="sep">|</span>
    <a href="#">About us</a><span class="sep">|</span>
    <a href="#">Products</a><span class="sep">|</span>
    <a href="#">Case studies</a><span class="sep">|</span>
    <a href="#">Ask for a demo</a><span class="sep">|</span>
    <a href="#">Contact us</a>
    <span class="search"><svg width="10" height="10" viewBox="0 0 10 10"><circle cx="4" cy="4" r="3" fill="none" stroke="#333" stroke-width="1.5"/><line x1="6.2" y1="6.2" x2="9.3" y2="9.3" stroke="#333" stroke-width="1.8"/></svg></span>
  </nav>
</header>

<section class="hero">
  <div class="hero-photo abs" role="img" aria-label="Photo of a young man looking up thoughtfully at the marketing services around him"></div>
  <div class="bubble" style="left:376px;top:111px;width:133px">Friendloop</div>
  <div class="bubble" style="left:603px;top:111px;width:134px">Website Design</div>
  <div class="bubble" style="left:47px;top:154px;width:100px">PPC</div>
  <div class="bubble" style="left:206px;top:145px;width:134px">Blogs/News</div>
  <div class="bubble" style="left:509px;top:175px;width:133px">Hosting</div>
  <div class="bubble" style="left:126px;top:212px;width:134px">Seekly Ads</div>
  <div class="bubble" style="left:525px;top:234px;width:101px">SEO</div>
  <div class="bubble" style="left:641px;top:233px;width:134px">Referrals</div>
  <div class="bubble" style="left:14px;top:255px;width:134px">Email Marketing</div>
  <div class="bubble" style="left:147px;top:296px;width:133px">Chirpwire Feeds</div>
  <div class="bubble" style="left:537px;top:297px;width:134px">Content Mangaement</div>
</section>

<section class="slider abs">
  <h1>Online Marketing Platform for Small Business</h1>
  <p>Cloud technology, high automation and our web expertise make it all possible.</p>
  <a class="learn-more" href="#">Learn more</a>
  <div class="dots"><i></i><i></i><i></i><i></i><i></i></div>
</section>

<section class="welcome abs">
  <h2><em>Welcome to</em><span class="brand-dot"></span>kVista</h2>
  <p class="narrow">Lorem ipsum dolor sit amet, consectetuer adipiscing elit, sed diam nonummy nibh euismod tincidunt ut laoreet dolore magna aliquam erat volutpat. Ut wisi enim ad minim veniam, quis nostrud exerci tation ullamcorper suscipit lobortis nisl ut aliquip ex ea commodo consequat.</p>
  <p class="narrow">Duis autem vel eum iriure dolor in hendrerit in vulputate velit esse molestie consequat, vel illum dolore eu feugiat nulla facilisis at vero eros et accumsan et iusto odio dignissim qui blandit praesent luptatum zzril delenit augue duis dolore te feugait nulla facilisi.</p>
  <p>Lorem ipsum dolor sit amet, consectetuer adipiscing elit, sed diam nonummy nibh euismod tincidunt ut laoreet dolore magna aliquam erat volutpat. Ut wisi enim ad minim veniam, quis nostrud exerci tation ullamcorper suscipit lobortis nisl ut aliquip ex ea commodo consequat.</p>
  <p>Duis autem vel eum iriure dolor in hendrerit in vulputate velit esse molestie consequat, vel illum dolore eu feugiat nulla facilisis at vero eros et accumsan et iusto odio dignissim qui blandit praesent luptatum zzril delenit augue duis dolore te feugait nulla facilisi.</p>
  <p>Nam liber tempor cum soluta nobis eleifend option congue nihil imperdiet doming id quod mazim placerat facer possim assum. Typi non habent claritatem insitam; est usus legentis in iis qui facit eorum claritatem. Investigationes demonstraverunt lectores legere me lius quod ii legunt saepius.</p>
</section>
<div class="sign-photo abs" role="img" aria-label="Photo of a businessman holding a sign with the company mark over his head"></div>

<aside class="news-box abs">
  <h3>We are launching a product that will revolutionize online marketing for SME's</h3>
  <div class="badge" style="left:49px;top:64px;width:58px;height:74px"></div>
  <div class="badge" style="left:95px;top:55px;width:62px;height:82px"></div>
  <div class="cap" style="left:52px;top:148px">2004, 2005, 2007, 2008</div>
  <div class="badge" style="left:49px;top:172px;width:123px;height:48px"></div>
  <div class="cap" style="left:52px;top:223px">Finalist<br>2004, 2005, 2006, 2009, 2010</div>
</aside>

<section class="features abs">
  <article class="feature" style="width:243px">
    <h4>OUR IDEA</h4>
    <div class="icon" role="img" aria-label="Illustration of a glowing light bulb" style="background:radial-gradient(circle at 50% 35%,#cfeaff,#6fb6e8 55%,#b59a4a)"></div>
    <h5>A simple but unique idea</h5>
    <p>We started kVista with a simple idea, to get online marketing to work for small businesses. We want to change the way small business owners acquire and keep customers.</p>
    <p>Cloud technology makes it all possible. It allows us to deliver a robust, scalable and highly automated system for a small monthly fee. It also allows for seamless integration with powerful sales tools while ensuring ease of use.</p>
  </article>
  <article class="feature" style="width:254px">
    <h4>OUR TEAM</h4>
    <div class="icon" role="img" aria-label="Illustration of a blue spotted mushroom character" style="background:radial-gradient(circle at 50% 35%,#8fd0ff,#1f7fd0 60%,#eee)"></div>
    <h5>Lots of experience &amp; knowledge</h5>
    <p>We are not an ISP or Hosting company. Nor are we a digital agency or designers. We come from a background of owning and growing businesses through online marketing. We understand sales.</p>
    <p>The kVista founder previously started up an e-commerce company and a telecommunication firm, both ranked among UK's 100 Fastest Growing Companies. And thanks to online marketing, both companies consistently outperformed much bigger rivals (e.g. Papercrest, Telcora, etc.) in growing sales.</p>
  </article>
  <article class="feature" style="width:245px;padding-left:12px">
    <h4>AWARDS</h4>
    <div class="icon" role="img" aria-label="Illustration of a folder with a blue star" style="background:linear-gradient(135deg,#e8e8e8,#5a6b80 60%,#2d6fc0)"></div>
    <h5>The Ideal Solution for small business</h5>
    <p style="margin-top:3px">We started with the idea that small business owners don't have the time nor resources to create an effective online presence. Most get by with basic, static websites that don't really work. It is easy to get lost in the world of online Pay-Per-Click (PPC) advertising, Search Engine Optimization (SEO), social media, online promotions, email marketing and content generation.</p>
    <p>We decided to create an affordable solution that allows a small business owner to manage all aspects of online marketing with a few clicks.</p>
  </article>
</section>

<footer class="site-footer abs">
  <div class="footer-col" style="left:101px">
    <h6>General Informations</h6>
    <ul><li>Home</li><li>About us</li><li>Products</li><li>Case Studies</li><li>News</li><li>Ask for a Demo</li></ul>
  </div>
  <div class="footer-col" style="left:282px">
    <h6>Products</h6>
    <ul><li>Website</li><li>Publish</li><li>Promote</li><li>Report</li></ul>
  </div>
  <div class="footer-col" style="left:397px">
    <h6>Follow us</h6>
    <div class="social"><i></i><i></i><i></i><i></i></div>
  </div>
  <div class="newsletter">
    <h6>SIGNUP FOR NEWSLETTER</h6>
    <div class="nl-form"><span></span><b>Subscribe</b></div>
  </div>
</footer>
<div class="mailbox abs" role="img" aria-label="Illustration of a metal mailbox"></div>
<div class="about-note abs">
  This is an exciting time to be part of the kVista team. We are well funded and we have an experienced management team with a track record of growing companies fast.
  <div class="brand"><span class="brand-dot"></span>kVista</div>
  23/2 Avenue<br>Street name<br>Country<br>email: info@kvista.com
</div>
<div class="legal abs">© 2012 kVista. All Rights Reserved. <a href="#">Terms &amp; Conditions</a><span class="sep">|</span><a href="#">Privacy Policy</a></div>

</body>
</html>
```